Summer Sale Graphics for Social Media

I want to create 11 social media graphics (new Instagram size 4:5 (1080 x 1350 pixels) focusing on our Summer Sale Graphics, using any of the pics attached. Use the attached pics, NO RANDOM STOCK PHOTOGRAPHY. For the color scheme of the graphics, they should all be complementary to the product colors in the photos.
You can add any of the photos attached but none are required. You can do some of the graphics in all text. I mainly need BOLD text that says one of the headlines (11 total) SEE ATTACHED WORD DOCUMENT for the headlines to use.

```html
<!DOCTYPE html>
<html lang="en">
<head>
<meta charset="utf-8">
<title>Summer Sale Social Graphics</title>
<link rel="stylesheet" href="https://fonts.googleapis.com/css2?family=Playfair+Display:wght@700&family=Arimo:wght@700&family=Roboto+Condensed:wght@700&display=swap">
<style>
  :root {
    --paper: #ffffff;
    --frame: #6d6d6d;
    --plum-head: #a0579c;
    --plum-sub: #c0589a;
    --plum-wave: #c9609a;
    --plum-band: #9c4677;
    --red-head: #c6373a;
    --red-sub: #ee2a2a;
    --red-wave: #f02b2f;
    --red-band: #bf3535;
    --navy-head: #3d2e6e;
    --navy-sub: #2d5ab5;
    --navy-wave: #2b5fb8;
    --navy-band: #3e2e6b;
    --pine-head: #264e45;
    --pine-sub: #5a9585;
    --pine-wave: #5a9585;
    --pine-band: #264e45;
  }
  * { margin: 0; padding: 0; box-sizing: border-box; }
  html, body { width: 1200px; height: 1200px; overflow: hidden; background: var(--paper); }
  .board { position: relative; width: 1200px; height: 1200px; }
  .post {
    position: absolute; width: 242px; height: 303px;
    background: var(--paper); border: 1px solid var(--frame); overflow: hidden;
  }
  .theme-plum { --head: var(--plum-head); --sub: var(--plum-sub); --wave: var(--plum-wave); --band: var(--plum-band); }
  .theme-red { --head: var(--red-head); --sub: var(--red-sub); --wave: var(--red-wave); --band: var(--red-band); }
  .theme-navy { --head: var(--navy-head); --sub: var(--navy-sub); --wave: var(--navy-wave); --band: var(--navy-band); }
  .theme-pine { --head: var(--pine-head); --sub: var(--pine-sub); --wave: var(--pine-wave); --band: var(--pine-band); }

  .tagline {
    position: absolute; left: 0; right: 0; text-align: center;
    font-family: "Arimo", Arial, sans-serif; font-weight: 700;
    font-size: 17.5px; line-height: 20px; color: var(--sub); white-space: nowrap;
  }
  .display {
    position: absolute; left: -20px; right: -20px; text-align: center;
    font-family: "Playfair Display", "Didot", serif; font-weight: 700;
    font-size: 82px; line-height: 1; letter-spacing: -0.045em;
    color: var(--head); white-space: nowrap;
  }
  .display.compact { font-size: 62px; letter-spacing: -0.06em; }
  .wave { position: absolute; left: 0; bottom: 0; width: 242px; height: 60px; display: block; }
  .wave .crest { fill: var(--wave); }
  .wave .base { fill: var(--band); }
  .offer {
    position: absolute; left: 24px; top: 277px;
    font-family: "Roboto Condensed", "Arial Narrow", sans-serif; font-weight: 700;
    font-size: 9.5px; line-height: 12px; color: var(--paper);
  }
  .offer.wide { font-family: "Arimo", Arial, sans-serif; font-size: 10.5px; left: 21px; }
</style>
</head>
<body>
<main class="board">

  <svg width="0" height="0" style="position:absolute" aria-hidden="true">
    <defs>
      <g id="wave-shape">
        <path class="crest" d="M0,23 C50,6 100,-2 150,8 C190,16 215,34 242,26 L242,60 L0,60 Z"/>
        <path class="base" d="M0,32 C60,20 120,22 165,33 C200,42 225,42 242,36 L242,60 L0,60 Z"/>
      </g>
    </defs>
  </svg>

  <!-- Row 1 -->
  <article class="post theme-plum" style="left:100px;top:135px">
    <p class="tagline" style="top:37px">Your Summer Body<br>Won't Wait</p>
    <p class="display" style="top:83px">SALE</p>
    <p class="display" style="top:151px">NOW!</p>
    <svg class="wave" viewBox="0 0 242 60" preserveAspectRatio="none"><use href="#wave-shape"/></svg>
    <p class="offer">Up to $15 OFF</p>
  </article>

  <article class="post theme-red" style="left:353px;top:135px">
    <p class="tagline" style="top:37px">Final Countdown<br>to Summer –</p>
    <p class="display" style="top:83px">SALE</p>
    <p class="display" style="top:151px">NOW!</p>
    <svg class="wave" viewBox="0 0 242 60" preserveAspectRatio="none"><use href="#wave-shape"/></svg>
    <p class="offer">Up to $15 OFF</p>
  </article>

  <article class="post theme-navy" style="left:605px;top:135px">
    <p class="display compact" style="top:10px">HURRY!</p>
    <p class="tagline" style="top:74px">Our Summer<br>Slim-Down<br>Sale Is On –</p>
    <p class="display compact" style="top:130px">DON'T</p>
    <p class="display compact" style="top:182px">MISS IT!</p>
    <svg class="wave" viewBox="0 0 242 60" preserveAspectRatio="none"><use href="#wave-shape"/></svg>
    <p class="offer">Up to $15 OFF</p>
  </article>

  <article class="post theme-pine" style="left:858px;top:135px">
    <p class="tagline" style="top:29px">Detox, Burn Fat,<br>and Turn Heads<br>This Summer</p>
    <p class="display" style="top:83px">SALE</p>
    <p class="display" style="top:151px">NOW!</p>
    <svg class="wave" viewBox="0 0 242 60" preserveAspectRatio="none"><use href="#wave-shape"/></svg>
    <p class="offer wide">Up to $15 OFF</p>
  </article>

  <!-- Row 2 -->
  <article class="post theme-plum" style="left:100px;top:448px">
    <p class="display" style="top:11px">SALE:</p>
    <p class="tagline" style="top:104px">Your Summer<br>Body Starts</p>
    <p class="display" style="top:141px">HERE</p>
    <svg class="wave" viewBox="0 0 242 60" preserveAspectRatio="none"><use href="#wave-shape"/></svg>
    <p class="offer">Up to $15 OFF</p>
  </article>

  <article class="post theme-red" style="left:353px;top:448px">
    <p class="tagline" style="top:32px">Summer's Here.<br>And We're<br>Having<br>the Biggest</p>
    <p class="display" style="top:110px">SALE</p>
    <p class="tagline" style="top:196px">of the Year</p>
    <svg class="wave" viewBox="0 0 242 60" preserveAspectRatio="none"><use href="#wave-shape"/></svg>
    <p class="offer">Up to $15 OFF</p>
  </article>

  <article class="post theme-navy" style="left:605px;top:448px">
    <p class="tagline" style="top:19px">Limited-Time<br>Summer</p>
    <p class="display" style="top:47px">SALE</p>
    <p class="tagline" style="top:132px">Snatch Your<br>Supplements</p>
    <p class="display" style="top:168px">NOW!</p>
    <svg class="wave" viewBox="0 0 242 60" preserveAspectRatio="none"><use href="#wave-shape"/></svg>
    <p class="offer">Up to $15 OFF</p>
  </article>

  <article class="post theme-pine" style="left:858px;top:448px">
    <p class="display" style="top:24px">ONE</p>
    <p class="display" style="top:89px">SALE.</p>
    <p class="tagline" style="top:173px">One Body.<br>One Summer<br>to Slay</p>
    <svg class="wave" viewBox="0 0 242 60" preserveAspectRatio="none"><use href="#wave-shape"/></svg>
    <p class="offer">Up to $15 OFF</p>
  </article>

  <!-- Row 3 -->
  <article class="post theme-plum" style="left:100px;top:761px">
    <p class="tagline" style="top:21px">Get Snatched<br>for Summer –<br>Supplements<br>On</p>
    <p class="display" style="top:90px">SALE</p>
    <p class="display" style="top:159px">NOW!</p>
    <svg class="wave" viewBox="0 0 242 60" preserveAspectRatio="none"><use href="#wave-shape"/></svg>
    <p class="offer">Up to $15 OFF</p>
  </article>

  <article class="post theme-red" style="left:353px;top:761px">
    <p class="tagline" style="top:21px">Summer Isn't<br>Waiting –<br>Neither<br>Should You</p>
    <p class="display" style="top:90px">SALE</p>
    <p class="display" style="top:159px">NOW!</p>
    <svg class="wave" viewBox="0 0 242 60" preserveAspectRatio="none"><use href="#wave-shape"/></svg>
    <p class="offer">Up to $15 OFF</p>
  </article>

  <article class="post theme-navy" style="left:605px;top:761px">
    <p class="tagline" style="top:21px">Slim Waist.<br>Flat Tummy.<br>More Energy.<br>Let's Go!</p>
    <p class="display" style="top:90px">SALE</p>
    <p class="display" style="top:159px">NOW!</p>
    <svg class="wave" viewBox="0 0 242 60" preserveAspectRatio="none"><use href="#wave-shape"/></svg>
    <p class="offer">Up to $15 OFF</p>
  </article>

</main>
</body>
</html>
```